Photographer's Rack Card - Contemporary With Style

My logo is already created, and exists in black and white only.
I need a 8.25in x 3.75in rack card designed to represent my photography business. It should be double-sided. I would like one side to have the logo prominent with maybe one image, the other side to have multiple images.
I specialize in Portrait, Wedding, and Commercial photography. I utilize bold, vivid, high-contrast tones to obtain striking images from bespoke portraits to luxury weddings, professional head shots, and custom corporate images. My style is designed to integrate with my clients’ demand for contemporary, stylish photography.
I will handle the printing on my own, using glossy card stock.
Check out my blog for my look: http://brettcalloway.ca/blog/
Logo is attached, samples of my work is attached.
Important info to include:
www.brettcalloway.ca
info@brettcalloway.ca
306.472.1538
Studio Address:
248 Birch Avenue W.
Suite 417
Moose Jaw, SK
Target Market(s)
This particular card is meant to attract all 3 of portrait, wedding, and commercial clients. I will have a specialized wedding card made later. Looking for more upscale type of client.
Industry/Entity Type
Business
Font styles to use
Requirements
Must have
- My logo as a prominent feature. Contemporary design. Bold.

```html
<!DOCTYPE html>
<html lang="en">
<head>
<meta charset="utf-8">
<title>Brett Calloway Photography – Rack Card</title>
<link rel="stylesheet" href="https://fonts.googleapis.com/css2?family=Josefin+Sans:wght@300;400&display=swap">
<style>
  :root {
    --stage: #3c3c3c;
    --card-front: #ffffff;
    --card-back: #8e8e8e;
    --ink-dark: #5a5a5a;
    --ink-light: #f4f4f4;
    --rule-dark: #8a8a8a;
    --rule-light: #e6e6e6;
  }
  * { margin: 0; padding: 0; box-sizing: border-box; }
  html, body {
    width: 1200px; height: 1000px; overflow: hidden;
    background: var(--stage);
    font-family: "Josefin Sans", sans-serif;
    font-weight: 300;
  }
  .canvas { position: relative; width: 1200px; height: 1000px; }
  .card { position: absolute; top: 22px; width: 434px; height: 955px; }
  .card--front { left: 156px; background: var(--card-front); }
  .card--back { left: 610px; background: var(--card-back); }

  .photo { position: absolute; }

  .wordmark { position: absolute; left: 0; width: 100%; text-align: center; font-weight: 300; }
  .wordmark__name { display: block; font-size: 33px; letter-spacing: 1px; line-height: 1; }
  .wordmark__trade { display: block; font-size: 15px; letter-spacing: 13px; margin-top: 20px; padding-left: 13px; line-height: 1; }
  .card--front .wordmark { top: 432px; color: var(--ink-dark); }
  .card--back .wordmark { top: 80px; color: var(--ink-light); }

  .services {
    position: absolute; top: 906px; left: 0; width: 100%;
    text-align: center; font-size: 16px; letter-spacing: 2px; color: var(--ink-dark);
  }
  .services span { margin: 0 8px; }

  .divider { position: absolute; top: 736px; height: 1px; background: var(--rule-light); }
  .divider--left { left: 38px; width: 158px; }
  .divider--right { left: 238px; width: 158px; }

  .contact { position: absolute; left: 252px; top: 773px; width: 136px; }
  .contact__title {
    text-align: center; font-size: 11px; letter-spacing: 2px; color: var(--ink-light);
    font-weight: 400; margin-bottom: 4px;
  }
  .contact__box {
    border: 1px solid var(--rule-light); height: 136px;
    padding: 14px 0 0 5px; color: var(--ink-light);
    font-size: 9.5px; line-height: 19px; letter-spacing: 1.2px;
  }
  .contact__box .spaced { letter-spacing: 2.4px; }
</style>
</head>
<body>
<main class="canvas">

  <section class="card card--front">
    <div class="photo" role="img" aria-label="Black and white portrait of two laughing children"
         style="left:0;top:0;width:434px;height:371px;background:linear-gradient(135deg,#4a4a4a 0%,#bdbdbd 45%,#e8e8e8 70%,#8c8c8c 100%);"></div>

    <div class="wordmark">
      <span class="wordmark__name">BRETT CALLOWAY</span>
      <span class="wordmark__trade">PHOTOGRAPHY</span>
    </div>

    <div class="photo" role="img" aria-label="Family of five standing in autumn grass under trees"
         style="left:0;top:563px;width:434px;height:308px;background:linear-gradient(180deg,#c9d3d6 0%,#8a6a3e 40%,#b98a3c 70%,#6b5122 100%);"></div>

    <p class="services">Portrait<span>|</span>Wedding<span>|</span>Commercial</p>
  </section>

  <section class="card card--back">
    <div class="wordmark">
      <span class="wordmark__name">BRETT CALLOWAY</span>
      <span class="wordmark__trade">PHOTOGRAPHY</span>
    </div>

    <div class="photo" role="img" aria-label="Groom and groomsmen in grey suits before a glass building"
         style="left:69px;top:199px;width:194px;height:127px;background:linear-gradient(180deg,#2f4a48 0%,#556a68 50%,#9a9c9a 100%);"></div>
    <div class="photo" role="img" aria-label="Toddler riding a vintage toy car on a lawn"
         style="left:266px;top:199px;width:109px;height:154px;background:linear-gradient(180deg,#a9b86a 0%,#c8b14a 35%,#6f8b3a 100%);"></div>
    <div class="photo" role="img" aria-label="Baby standing on a grey armchair in a bright studio"
         style="left:69px;top:329px;width:194px;height:271px;background:linear-gradient(180deg,#d5d8da 0%,#b9bcbe 55%,#6f7173 85%,#a7a7a7 100%);"></div>
    <div class="photo" role="img" aria-label="Woman in a dark dress seated on a leather sofa"
         style="left:266px;top:356px;width:109px;height:165px;background:linear-gradient(160deg,#6a4a34 0%,#9a5a2c 50%,#3a2418 100%);"></div>
    <div class="photo" role="img" aria-label="Woman in a blue dress beside a fountain at dusk"
         style="left:266px;top:524px;width:109px;height:166px;background:linear-gradient(180deg,#5e5a4c 0%,#b89a6c 45%,#8a7d6a 100%);"></div>
    <div class="photo" role="img" aria-label="Team in red jackets posing against a blue backdrop"
         style="left:69px;top:603px;width:194px;height:87px;background:linear-gradient(180deg,#2d4560 0%,#9a2a2e 60%,#6a1e22 100%);"></div>

    <div class="divider divider--left"></div>
    <div class="divider divider--right"></div>

    <div class="contact">
      <p class="contact__title">CONTACT</p>
      <div class="contact__box">
        www.brettcalloway.ca<br>
        info@brettcalloway.ca<br>
        <span class="spaced">Ph: 306.472.1538</span><br>
        <span class="spaced">Studio Address:</span><br>
        <span class="spaced">248 Birch Avenue W.</span><br>
        Suite 417 Moose Jaw, SK
      </div>
    </div>
  </section>

</main>
</body>
</html>
```